Business card design needed

I have started a new business called Marlow Auto Electrical, although the words Marlow Auto Electrical will be used on signage and documents I actually want to market the business as MAE. The services I offer are Mobile Auto Electrical, Automotive Air Conditioning and Test And Tag. My business will be targetting the Mining Industry, Civil, Rail, Agricultural and Workshop Testing And Tagging. My auto electrical service ranges from fault finding to new vehicle and mine compliance fit outs. I have a very strong focus on quality workmanship. I will upload the logo I have designed and want to use I am happy for the logo colour to change but the design itself must stay the same. I want the design to have a modern, eye catching, energetic feel. As I am a passionate motorsport fan I am happy for this to also influence the design. I am happy for the front of the card to have only the emblem and logo design and the back to have all the info.

Industry/Entity Type

Electrical

Contact Information for Business Card

MAE Marlow Auto Electrical, Glen Tavish, Auto Electrician, Mobile No 0417268354

Requirements
Must have
• On the business card it is mandatory that the following license numbers are shown:

MVRL83742
PXB L731406
ABN 48 913 260 154

```html
<!DOCTYPE html>
<html lang="en">
<head>
<meta charset="utf-8">
<title>Marlow Auto Electrical – Business Card</title>
<link rel="stylesheet" href="https://fonts.googleapis.com/css2?family=Arimo:wght@400;700&display=swap">
<style>
  :root {
    --stage: #d9d4cc;
    --card: #0d0d0d;
    --accent: #f6ae0f;
    --ink-light: #f2f2f2;
    --ink-dark: #1a1a1a;
    --font: "Arimo", Arial, sans-serif;
  }
  * { box-sizing: border-box; margin: 0; padding: 0; }
  html, body {
    width: 1200px;
    height: 900px;
    overflow: hidden;
    background: var(--stage);
    font-family: var(--font);
  }
  .stage {
    width: 1200px;
    height: 900px;
    display: flex;
    flex-direction: column;
    align-items: center;
    justify-content: center;
    gap: 60px;
  }
  .card {
    position: relative;
    width: 620px;
    height: 354px;
    background: var(--card);
    border-radius: 4px;
    box-shadow: 0 10px 28px rgba(0, 0, 0, 0.28);
    overflow: hidden;
  }

  /* Company name */
  .brand {
    display: flex;
    align-items: center;
    gap: 12px;
    color: var(--accent);
    font-weight: 700;
    text-transform: uppercase;
    white-space: nowrap;
  }
  .brand__square {
    flex: none;
    background: var(--accent);
  }

  /* Front */
  .card--front {
    display: flex;
    align-items: center;
    justify-content: center;
  }
  .card--front .brand {
    font-size: 30px;
    letter-spacing: 1.5px;
  }
  .card--front .brand__square {
    width: 22px;
    height: 22px;
  }

  /* Back */
  .card--back .brand {
    position: absolute;
    top: 30px;
    left: 30px;
    gap: 8px;
    font-size: 15px;
    letter-spacing: 1px;
  }
  .card--back .brand__square {
    width: 12px;
    height: 12px;
  }
  .contact {
    position: absolute;
    right: 40px;
    top: 120px;
    text-align: right;
    text-transform: uppercase;
  }
  .contact__name {
    color: var(--accent);
    font-size: 26px;
    font-weight: 400;
    letter-spacing: 1px;
  }
  .contact__role {
    color: var(--ink-light);
    font-size: 16px;
    letter-spacing: 1px;
    margin-top: 2px;
  }
  .contact__phone {
    color: var(--ink-light);
    font-size: 13px;
    letter-spacing: 1px;
    margin-top: 16px;
  }
  .licence-band {
    position: absolute;
    left: 0;
    right: 0;
    bottom: 0;
    height: 46px;
    background: var(--accent);
    display: flex;
    align-items: center;
    justify-content: space-between;
    padding: 0 30px;
    color: var(--ink-dark);
    font-size: 12px;
    letter-spacing: 1px;
    text-transform: uppercase;
  }
</style>
</head>
<body>
<main class="stage">
  <section class="card card--front" aria-label="Card front">
    <p class="brand">
      <span class="brand__square" aria-hidden="true"></span>
      <span class="brand__name">Marlow Auto Electrical</span>
    </p>
  </section>

  <section class="card card--back" aria-label="Card back">
    <p class="brand">
      <span class="brand__square" aria-hidden="true"></span>
      <span class="brand__name">Marlow Auto Electrical</span>
    </p>
    <div class="contact">
      <h1 class="contact__name">Glen Tavish</h1>
      <p class="contact__role">Auto Electrician</p>
      <p class="contact__phone">Mobile:&nbsp; 0417268354</p>
    </div>
    <div class="licence-band">
      <span class="licence">ABN 48 913 260 154</span>
      <span class="licence">PXB L731406</span>
      <span class="licence">MVRL83742</span>
    </div>
  </section>
</main>
</body>
</html>
```